Your Vorrant App all-in-one system for transformation needs a book cover.

Hello- I would like a very similar book cover ( Beneath The Quiet Orchard book cover) as the sample I'm attaching. The person on my book cover would be less stiff, wear a cowboy hat, and maybe have flying hair. High-end bohemian style. Our brand colors are gold, light pink, and tan color. I'll attach App Logo and the colors we used on that. The title of my book is: "The Radiant Harbor Practice" and I will also need formatting for ebook, audio, and paperback. Thank you, Lorna

Target Market(s)

Those who are on the path to enlightenment - 60% women 40% men

Industry/Entity Type

Consciousness Industry

Font styles to use
Other font styles liked:
• Dubai

Colors
0054AA
0677BA
7BADD7
CADEEF
E8F1F8
FFC000
F8CF3A
FAE287
FDF2CF
FEFAEE
F0912C
F2A743
F7CA91
FBE8D2
FDF5EE
EE7325
F08F49
F5BC92
FAE3D3
FDF4ED
6B429C
8869AF
B7A5CE
E3DAEB
F3F0F8

Requirements
Must have
• Light spheres - light pink, orange-pink, gold and possibly blue on the very top
Should not have
• More of a sun rise feel, less or no clouds in the upper section,

```html
<!DOCTYPE html>
<html lang="en">
<head>
<meta charset="utf-8">
<title>The Radiant Harbor Practice – Cover Versions</title>
<link rel="stylesheet" href="https://fonts.googleapis.com/css2?family=Open+Sans:wght@600;700;800&family=Yellowtail&display=swap">
<style>
  :root {
    --board: #a3a3a3;
    --label: #c4c4c4;
    --white: #ffffff;
    --red: #c4161c;
    --navy-script: #1d5a88;
    --sky-script: #4aa8e0;
    --sky-line: #5cb5ec;
    --author: #cdb79c;
    --ground: #1c1008;
    --badge: #fbf6f2;
  }
  * { margin: 0; padding: 0; box-sizing: border-box; }
  html, body {
    width: 1200px; height: 509px; overflow: hidden;
    background: var(--board);
    font-family: "Open Sans", Arial, sans-serif;
  }
  .board { position: relative; width: 1200px; height: 509px; }

  .cover {
    position: absolute; top: 30px; width: 271px; height: 407px;
    overflow: hidden;
    box-shadow: 6px 8px 12px rgba(0,0,0,.35);
  }
  .cover--v1 { left: 29px; }
  .cover--v2 { left: 316px; }
  .cover--v3 { left: 604px; }
  .cover--v4 { left: 897px; }

  .cover__scene { position: absolute; inset: 0; }
  .cover--v1 .cover__scene {
    background:
      radial-gradient(ellipse 38% 20% at 45% 78%, rgba(255,250,225,.95), rgba(255,220,160,.55) 45%, rgba(255,190,130,0) 100%),
      linear-gradient(to bottom, rgba(0,0,0,0) 72%, #4a2412 80%, var(--ground) 100%),
      linear-gradient(to bottom, #ffbba0 0%, #fbae93 40%, #f8a283 58%, #fbd3ad 72%);
  }
  .cover--v2 .cover__scene {
    background:
      radial-gradient(ellipse 38% 20% at 45% 78%, rgba(255,250,225,.95), rgba(255,220,160,.55) 45%, rgba(255,190,130,0) 100%),
      linear-gradient(to bottom, rgba(0,0,0,0) 72%, #4a2412 80%, var(--ground) 100%),
      linear-gradient(to bottom, #357ea2 0%, #8fa3b0 22%, #e9a596 40%, #f7a285 58%, #fbd3ad 72%);
  }
  .cover--v3 .cover__scene {
    background:
      radial-gradient(ellipse 38% 20% at 45% 78%, rgba(255,250,225,.95), rgba(255,220,160,.55) 45%, rgba(255,190,130,0) 100%),
      linear-gradient(to bottom, rgba(0,0,0,0) 72%, #4a2412 80%, var(--ground) 100%),
      linear-gradient(to bottom, #5a9fc6 0%, #6eadd0 35%, #b7d3df 55%, #f4dcbc 68%, #fbd7ad 74%);
  }
  .cover--v4 .cover__scene {
    background:
      radial-gradient(ellipse 38% 20% at 45% 78%, rgba(255,250,225,.95), rgba(255,220,160,.55) 45%, rgba(255,190,130,0) 100%),
      linear-gradient(to bottom, rgba(0,0,0,0) 72%, #4a2412 80%, var(--ground) 100%),
      linear-gradient(to bottom, #cbe2f0 0%, #cfe3ee 40%, #e6e6dc 58%, #f8dbb5 72%);
  }

  .cover__badge {
    position: absolute; top: 17px; right: 17px; width: 30px; height: 30px;
    background: var(--badge); border-radius: 4px;
    display: flex; align-items: center; justify-content: center;
    font-size: 6.5px; font-weight: 700; color: var(--red);
    box-shadow: 0 1px 2px rgba(0,0,0,.15);
  }

  .title { position: absolute; left: 0; right: 0; text-align: center; }
  .title__line {
    position: absolute; left: 0; right: 0;
    font-weight: 800; line-height: 1; letter-spacing: -0.5px;
    color: var(--white);
  }
  .title__the { top: 44px; font-size: 29px; }
  .title__script {
    top: 40px; font-family: "Yellowtail", cursive; font-weight: 400;
    font-size: 36px; letter-spacing: 0;
  }
  .title__main-1 { top: 74px; font-size: 42px; }
  .title__main-2 { top: 108px; font-size: 42px; }
  .title__main-3 { top: 146px; font-size: 32px; }

  .cover--v3 .title__script { color: var(--navy-script); }
  .cover--v3 .title__main-1,
  .cover--v3 .title__main-2,
  .cover--v3 .title__main-3 { color: var(--red); }
  .cover--v4 .title__script { color: var(--sky-script); }
  .cover--v4 .title__main-1,
  .cover--v4 .title__main-2 { color: var(--red); }
  .cover--v4 .title__main-3 { color: var(--sky-line); }

  .cover__author {
    position: absolute; left: 0; right: 0; top: 367px;
    text-align: center; font-size: 22px; font-weight: 700;
    letter-spacing: 5px; color: var(--author); opacity: .9;
  }

  .version-label {
    position: absolute; top: 468px; width: 271px; text-align: center;
    font-size: 13px; font-weight: 700; color: var(--label);
  }
</style>
</head>
<body>
<main class="board">

  <article class="cover cover--v1">
    <div class="cover__scene" role="img" aria-label="Sunrise photo: silhouette of a woman in a hat with flowing hair standing in tall grass among glowing light spheres"></div>
    <div class="cover__badge">Vorrant</div>
    <h1 class="title">
      <span class="title__line title__the">THE</span>
      <span class="title__line title__main-1">RADIANT</span>
      <span class="title__line title__main-2">HARBOR</span>
      <span class="title__line title__main-3">PRACTICE</span>
    </h1>
    <p class="cover__author">LORNA</p>
  </article>

  <article class="cover cover--v2">
    <div class="cover__scene" role="img" aria-label="Sunrise photo with blue-to-pink sky: silhouette of a woman in a hat among glowing light spheres"></div>
    <div class="cover__badge">Vorrant</div>
    <h1 class="title">
      <span class="title__line title__script">The</span>
      <span class="title__line title__main-1">RADIANT</span>
      <span class="title__line title__main-2">HARBOR</span>
      <span class="title__line title__main-3">PRACTICE</span>
    </h1>
    <p class="cover__author">LORNA</p>
  </article>

  <article class="cover cover--v3">
    <div class="cover__scene" role="img" aria-label="Sunrise photo with blue sky: silhouette of a woman in a hat among glowing light spheres"></div>
    <div class="cover__badge">Vorrant</div>
    <h1 class="title">
      <span class="title__line title__script">The</span>
      <span class="title__line title__main-1">RADIANT</span>
      <span class="title__line title__main-2">HARBOR</span>
      <span class="title__line title__main-3">PRACTICE</span>
    </h1>
    <p class="cover__author">LORNA</p>
  </article>

  <article class="cover cover--v4">
    <div class="cover__scene" role="img" aria-label="Sunrise photo with pale blue sky: silhouette of a woman in a hat among glowing light spheres"></div>
    <div class="cover__badge">Vorrant</div>
    <h1 class="title">
      <span class="title__line title__script">The</span>
      <span class="title__line title__main-1">RADIANT</span>
      <span class="title__line title__main-2">HARBOR</span>
      <span class="title__line title__main-3">PRACTICE</span>
    </h1>
    <p class="cover__author">LORNA</p>
  </article>

  <p class="version-label" style="left:29px">VERSION 1</p>
  <p class="version-label" style="left:316px">VERSION 2</p>
  <p class="version-label" style="left:604px">VERSION 3</p>
  <p class="version-label" style="left:897px">VERSION 4</p>

</main>
</body>
</html>
```